TV - business card

Tidewell Vantage is an insurance brokerage firm, inovative, proactive, vigorous, which aims to become the leader of the insurance brokers in Anfrica. We should like to get some designs which should be avoided also in Gray / Metallic for the Administration and Orange / Blue for the Managers (ike in the picture sent). The Blue / Green logo is not the correct one, but the source of the file. Please adjust the color accordingly for the business cards. 1 / Orange / Blue 2 / Gray / Metallic We want something classic but which is transmitted strenght, inovation, modernity and most of all, rapidity. We want something start-up like, very punchy and catching eye remaining profesional at the same time. Name: Delton Ashgrove Function: Managing Director Address: N ° 73/74 Cmt. Bolembe - R / C 2B Esquerda - Bairro Quimbuta - Luanda Tel: (+244) 947 385 619 Email: delton.ashgrove@tidewell-v.com Website: www.tidewell-v. com We want classic in the front and creative, colorfull at the back. The cards will be printed in relief, with very high quality of paper.
Industry/Entity Type
Insurance Broker
Colors
Designer to choose colors to be used in the design.
Look and feel

```html
<!DOCTYPE html>
<html lang="en">
<head>
<meta charset="utf-8">
<title>Tidewell Vantage – Business Card</title>
<link rel="stylesheet" href="https://fonts.googleapis.com/css2?family=Exo+2:wght@700&family=Roboto:wght@400&display=swap">
<style>
  :root {
    --orange: #f24e35;
    --blue: #2ea7e0;
    --ink: #333333;
    --paper: #ffffff;
    --backdrop-light: #e4e4e4;
    --backdrop-dark: #bdbdbd;
  }
  * { margin: 0; padding: 0; box-sizing: border-box; }
  html, body { width: 1200px; height: 801px; overflow: hidden; }
  body {
    background: radial-gradient(ellipse at 40% 20%, var(--backdrop-light), var(--backdrop-dark));
    position: relative;
    font-family: "Roboto", sans-serif;
  }
  .card {
    position: absolute;
    top: 252px;
    width: 520px;
    height: 297px;
    box-shadow: 0 8px 24px rgba(0,0,0,0.18);
  }
  .card--front { left: 60px; background: var(--paper); }
  .card--back { left: 620px; background: var(--orange); }

  .brand {
    position: absolute;
    top: 44px;
    left: 250px;
    display: flex;
    align-items: center;
    gap: 10px;
  }
  .brand__dot {
    width: 26px; height: 26px; border-radius: 50%;
    background: var(--orange);
  }
  .brand__name {
    font-family: "Exo 2", sans-serif;
    font-weight: 700;
    font-size: 22px;
    letter-spacing: 0.5px;
    color: var(--orange);
    text-transform: uppercase;
  }

  .person { position: absolute; left: 30px; top: 108px; }
  .person__name {
    font-family: "Exo 2", sans-serif;
    font-weight: 700;
    font-size: 23px;
    color: var(--orange);
    line-height: 1;
  }
  .person__role {
    font-size: 13px;
    color: var(--blue);
    margin-top: 4px;
  }

  .divider {
    position: absolute;
    left: 30px; right: 30px; top: 165px;
    height: 1px;
    background: var(--ink);
  }

  .contacts {
    position: absolute; left: 30px; top: 178px;
    list-style: none;
    font-size: 12px;
    color: var(--ink);
  }
  .contacts li { display: flex; align-items: center; gap: 8px; height: 19px; }
  .contacts svg { width: 11px; height: 11px; flex: none; }

  .address {
    position: absolute; right: 30px; top: 178px;
    font-size: 12px;
    line-height: 19px;
    color: var(--ink);
    text-align: right;
    font-style: normal;
  }

  .back-brand {
    position: absolute;
    left: 0; right: 0; top: 104px;
    display: flex; justify-content: center; align-items: center; gap: 12px;
  }
  .back-brand__dot {
    width: 36px; height: 36px; border-radius: 50%;
    border: 3px solid var(--paper);
  }
  .back-brand__name {
    font-family: "Exo 2", sans-serif;
    font-weight: 700;
    font-size: 28px;
    color: var(--paper);
    text-transform: uppercase;
  }
  .back-url {
    position: absolute; left: 0; right: 0; top: 222px;
    text-align: center;
    font-size: 14px;
    letter-spacing: 4px;
    color: var(--paper);
  }
</style>
</head>
<body>

<section class="card card--front" aria-label="Card front">
  <div class="brand">
    <span class="brand__dot"></span>
    <span class="brand__name">Tidewell-Vantage</span>
  </div>

  <div class="person">
    <p class="person__name">Delton Ashgrove</p>
    <p class="person__role">Managing Director</p>
  </div>

  <div class="divider"></div>

  <ul class="contacts">
    <li>
      <svg viewBox="0 0 12 12" aria-hidden="true"><path fill="var(--orange)" d="M2.5 1 4.5 1 5 4 3.8 5A7 7 0 0 0 7 8.2L8 7l3 .5v2C11 10.3 10.3 11 9.5 11A8.5 8.5 0 0 1 1 2.5C1 1.7 1.7 1 2.5 1Z"/></svg>
      (+244) 947 385 619
    </li>
    <li>
      <svg viewBox="0 0 12 12" aria-hidden="true"><rect x="0.5" y="2" width="11" height="8" fill="var(--orange)"/><path d="M1 2.5 6 6.5 11 2.5" fill="none" stroke="#fff" stroke-width="1"/></svg>
      delton.ashgrove@tidewell-v.com
    </li>
    <li>
      <svg viewBox="0 0 12 12" aria-hidden="true"><circle cx="6" cy="6" r="5.5" fill="var(--orange)"/><path d="M0.5 6h11M6 .5c-3 3-3 8 0 11M6 .5c3 3 3 8 0 11" fill="none" stroke="#fff" stroke-width="0.8"/></svg>
      www.tidewell-v.com
    </li>
  </ul>

  <address class="address">
    N° 73/74 Cmt. Bolembe<br>
    R / C 2B Esquerda<br>
    Bairro Quimbuta, Luanda
  </address>
</section>

<section class="card card--back" aria-label="Card back">
  <div class="back-brand">
    <span class="back-brand__dot"></span>
    <span class="back-brand__name">Tidewell Vantage</span>
  </div>
  <p class="back-url">WWW.TIDEWELL-V.COM</p>
</section>

</body>
</html>
```